Social Media Graphics - ALL TEXT RK

We are looking for a series of social media graphics for Instagram (standard size 1:1 (1080x1080px) that are ALL TEXT. We want the following quotes below on each graphic; one quote per graphic. AND, In very small letters at the bottom of each graphic, add @RKMarlowLive

The look and feel of these graphics should be complimentary to the color palette attached below; but keep them simple. But the design is up to you; at the end of this document, I provided various samples of all text graphics that I like as examples.

Target Market(s)

women looking to lose weight

Industry/Entity Type

health and wellness

Colors
E54698
E96AAD
F1A4CE
F9D9EA
FCEFF6

Requirements
Must have
• the quotes in the document
Should not have
• no stock photography

```html
<!DOCTYPE html>
<html lang="en">
<head>
<meta charset="utf-8">
<title>RK Social Graphics – All Text Series</title>
<link href="https://fonts.googleapis.com/css2?family=Montserrat:wght@700;800;900&family=Oswald:wght@600;700&display=swap" rel="stylesheet">
<style>
  :root{
    --board:#414143;
    --white:#ffffff;
    --pink-hot:#ec0f7e;
    --pink-mid:#e54698;
    --pink-soft:#e96aad;
    --pink-light:#f1a4ce;
    --pink-pale:#f9d9ea;
    --pink-mist:#fceff6;
    --magenta-deep:#9c0a4f;
    --berry:#c4125f;
    --shadow-pink:#c2105f;
  }
  *{box-sizing:border-box;margin:0;padding:0}
  html,body{width:1200px;height:932px;overflow:hidden;background:var(--board)}
  .board{position:relative;width:1200px;height:932px}
  .post{position:absolute;width:343px;height:343px;overflow:hidden;color:var(--white);
    font-family:"Montserrat",sans-serif;font-weight:800;text-transform:uppercase;
    box-shadow:0 10px 14px -6px rgba(0,0,0,.45)}
  .post .line{position:absolute;line-height:1;white-space:nowrap}
  .handle{position:absolute;font-weight:700;text-transform:none;font-size:9px;letter-spacing:.2px}

  /* 1 — wake up tomorrow */
  .post--wake{left:57px;top:65px;
    background:radial-gradient(circle at 62% 18%,#ff5fb0 0,#f6339a 30%,#e0157e 60%,#b80a63 100%)}
  .post--wake .line{left:25px}
  .tag-box{background:var(--white);color:var(--pink-hot);padding:0 5px}

  /* 2 — struggling */
  .post--struggle{left:434px;top:65px;
    background:linear-gradient(165deg,#f56cb0 0%,#f3409c 45%,#ec0f7e 100%)}
  .post--struggle .line{right:23px;text-align:right}
  .rule{position:absolute;background:var(--white)}

  /* 3 — one supplement */
  .post--night{left:811px;top:65px;
    background:radial-gradient(circle at 15% 95%,#7a0634 0,#a1124e 35%,#c8126a 70%,#e0167a 100%)}
  .night-block{position:absolute;left:10px;top:40px;width:320px;text-align:center;transform:rotate(-9deg);transform-origin:center}
  .night-block .row{display:block;line-height:1.02}
  .night-block .stamp{display:inline-block;background:var(--white);color:var(--magenta-deep);padding:2px 8px;margin:2px 0 8px}
  .night-block .underline{display:block;width:150px;height:2px;background:var(--white);margin:4px auto 0}
  .handle-chip{position:absolute;left:240px;top:313px;width:103px;height:19px;background:var(--pink-mist);color:var(--berry);
    font-size:8px;font-weight:800;display:flex;align-items:center;padding-left:6px;text-transform:none}

  /* 4 — finally a natural solution */
  .post--finally{left:57px;top:503px;
    background:linear-gradient(150deg,#ff1e8f 0%,#f7148a 45%,#ec127f 75%,#f03a96 100%)}
  .post--finally .line,.post--weight .line{font-family:"Oswald",sans-serif;font-weight:700;letter-spacing:-.3px}
  .post--finally .line{left:0;width:343px;text-align:center}
  .frame{position:absolute;left:0;top:0}

  /* 5 — hormones */
  .post--weight{left:434px;top:503px;
    background:linear-gradient(160deg,#8c0f5a 0%,#b5146b 25%,#e0157d 55%,#ee1f74 85%,#f0325a 100%)}
  .post--weight .line{left:25px}
  .weight-band{position:absolute;left:0;top:195px;width:206px;height:51px;background:var(--white)}

  /* 6 — frustrated */
  .post--frustrated{left:811px;top:503px;
    background:linear-gradient(155deg,#f46db3 0%,#f84aa4 40%,#f6339a 65%,#f968b2 100%)}
  .post--frustrated .line{left:25px;text-shadow:1px 1px 0 var(--shadow-pink),2px 2px 0 var(--shadow-pink)}
  .deco{position:absolute;left:0;top:0}
</style>
</head>
<body>
<main class="board">

  <!-- 1 -->
  <section class="post post--wake">
    <span class="line tag-box" style="top:65px;font-size:19px;height:21px;line-height:21px">Wake up</span>
    <span class="line" style="top:88px;font-size:28px">Tomorrow</span>
    <span class="line" style="top:114px;font-size:20px">With a flatter</span>
    <span class="line" style="top:135px;font-size:22px">Belly- yes</span>
    <span class="line" style="top:161px;font-size:15px">This overnight</span>
    <span class="line tag-box" style="top:180px;font-size:34px;height:34px;line-height:34px;padding:0 3px">Remedy</span>
    <span class="line" style="top:216px;font-size:23px">Works</span>
    <span class="line" style="top:241px;font-size:23px">Like magic!</span>
    <span class="handle" style="left:25px;top:317px">@RKMarlowLive</span>
  </section>

  <!-- 2 -->
  <section class="post post--struggle">
    <span class="line" style="top:62px;font-size:26px">Struggling</span>
    <span class="line" style="top:91px;font-size:19px">With bloating</span>
    <span class="line" style="top:115px;font-size:19px">and belly fat?</span>
    <span class="line" style="top:153px;font-size:22px">Try this</span>
    <span class="line" style="top:178px;font-size:33px">Natural</span>
    <span class="line" style="top:211px;font-size:15px">Solution tonight</span>
    <span class="line" style="top:231px;font-size:19px">and wake up</span>
    <span class="line" style="top:256px;font-size:20px">Feeling lighter!</span>
    <span class="rule" style="left:163px;top:277px;width:157px;height:2px"></span>
    <span class="handle" style="right:23px;top:316px;font-size:8.5px;font-weight:800">@RKMarlowLive</span>
    <span class="rule" style="left:245px;top:329px;width:78px;height:2px"></span>
  </section>

  <!-- 3 -->
  <section class="post post--night">
    <div class="night-block">
      <span class="row" style="font-size:17px">One supplement</span>
      <span class="row" style="font-size:35px;font-weight:900">One night</span>
      <span class="row" style="font-size:24px">Your belly bloat</span>
      <span class="row" style="font-size:24px">could be gone</span>
      <span class="stamp" style="font-size:33px;font-weight:900">By morning</span>
      <span class="row" style="font-size:22px">Here’s</span>
      <span class="row" style="font-size:24px">How it works!</span>
      <span class="underline"></span>
    </div>
    <span class="handle-chip">@RKMarlowLive</span>
  </section>

  <!-- 4 -->
  <section class="post post--finally">
    <svg class="frame" width="343" height="343" viewBox="0 0 343 343" aria-hidden="true">
      <polyline points="82,50 38,50 38,293 82,293" fill="none" stroke="#fff" stroke-width="2"/>
      <polyline points="262,50 305,50 305,293 262,293" fill="none" stroke="#fff" stroke-width="2"/>
    </svg>
    <span class="line" style="top:86px;font-size:31px">Finally-A</span>
    <span class="line" style="top:116px;font-size:26px">Natural solution</span>
    <span class="line" style="top:144px;font-size:22px">That flattens</span>
    <span class="line" style="top:175px;font-size:25px">Your belly</span>
    <span class="line" style="top:201px;font-size:25px">And eases</span>
    <span class="line" style="top:227px;font-size:31px">Stomach bloat</span>
    <span class="handle" style="left:0;width:343px;text-align:center;top:290px;font-family:'Oswald',sans-serif;font-size:12px;font-weight:600">@RKMarlowLive</span>
  </section>

  <!-- 5 -->
  <section class="post post--weight">
    <span class="weight-band"></span>
    <span class="line" style="top:59px;font-size:45px">Sis,</span>
    <span class="line" style="top:106px;font-size:30px">Your hormones</span>
    <span class="line" style="top:138px;font-size:24px">Are out of whack</span>
    <span class="line" style="top:168px;font-size:27px">That's why the</span>
    <span class="line" style="top:196px;font-size:50px;color:var(--pink-hot)">Weight</span>
    <span class="line" style="top:248px;font-size:31px">Won't budge!</span>
    <span class="handle" style="left:28px;top:316px;font-family:'Oswald',sans-serif;font-size:12px;font-weight:600">@RKMarlowLive</span>
  </section>

  <!-- 6 -->
  <section class="post post--frustrated">
    <svg class="deco" width="343" height="343" viewBox="0 0 343 343" aria-hidden="true">
      <g stroke="#fff" stroke-opacity=".12" stroke-width="28" stroke-linecap="round" fill="none">
        <line x1="110" y1="-10" x2="190" y2="60"/>
        <line x1="190" y1="-10" x2="270" y2="70"/>
        <line x1="340" y1="20" x2="280" y2="80"/>
      </g>
      <polygon points="180,230 230,280 343,170 343,200 230,310" fill="#d81a7a" fill-opacity=".25"/>
    </svg>
    <span class="line" style="top:75px;font-size:30px">Frustrated</span>
    <span class="line" style="top:105px;font-size:19px">With belly fat</span>
    <span class="line" style="top:125px;font-size:19px">That won't budge?</span>
    <span class="line" style="top:153px;font-size:26px">I've got the</span>
    <span class="line" style="top:181px;font-size:17px">Solution that finally</span>
    <span class="line" style="top:200px;font-size:34px">Worked</span>
    <span class="line" style="top:232px;font-size:16px">For me-no crazy</span>
    <span class="line" style="top:251px;font-size:19px">Diets required</span>
    <span class="handle" style="left:25px;top:316px;font-size:11px">@RKMarlowLive</span>
  </section>

</main>
</body>
</html>
```